ALL TEXT GRAPHICS TM May 2025 for Instagram

We are looking for a series of social media graphics for Instagram (new size: 4:5 (1080 x 1350 pixels) ratio that are ALL TEXT. We want the following quotes below on each graphic; one quote per graphic. AND, In very small letters at the bottom of each graphic, add @TovaMarshOnline
The look and feel of these graphics should be complimentary to the color palette attached below; but keep them simple. But the design is up to you; at the end of this document, I provided various samples of all text graphics that I like as examples.
Target Market(s)
women looking to lose weight
Look and feel

```html
<!DOCTYPE html>
<html lang="en">
<head>
<meta charset="utf-8">
<title>You're Next – Tova Marsh</title>
<link rel="stylesheet" href="https://fonts.googleapis.com/css2?family=Cinzel:wght@400&family=DM+Serif+Display&display=swap">
<style>
  :root {
    --bg: #ffffff;
    --pink-bright: #ff3fa4;
    --pink-deep: #d6086f;
    --pink-soft: #ff8ec8;
    --ink: #2b2b2b;
  }
  html, body {
    margin: 0;
    padding: 0;
    overflow: hidden;
    background: var(--bg);
  }
  .post {
    position: relative;
    width: 960px;
    height: 1200px;
    background: var(--bg);
    overflow: hidden;
  }
  .intro {
    position: absolute;
    left: 98px;
    top: 131px;
    margin: 0;
    font-family: "DM Serif Display", serif;
    font-weight: 400;
    font-size: 72px;
    line-height: 76px;
    letter-spacing: -0.04em;
    color: var(--pink-bright);
    white-space: nowrap;
  }
  .promise {
    position: absolute;
    left: 97px;
    top: 441px;
    margin: 0;
    font-family: "Cinzel", serif;
    font-weight: 400;
    font-size: 86px;
    line-height: 102px;
    letter-spacing: -0.02em;
    word-spacing: 0.08em;
    color: var(--pink-deep);
    text-transform: uppercase;
    white-space: nowrap;
  }
  .call {
    position: absolute;
    left: 96px;
    top: 842px;
    margin: 0;
    font-family: "Cinzel", serif;
    font-weight: 400;
    font-size: 120px;
    line-height: 120px;
    letter-spacing: -0.03em;
    color: var(--ink);
    white-space: nowrap;
  }
  .sparkles {
    position: absolute;
    left: 790px;
    top: 730px;
    width: 150px;
    height: 140px;
  }
  .divider {
    position: absolute;
    left: 109px;
    top: 1044px;
    width: 93px;
    height: 5px;
    background: var(--pink-soft);
  }
  .handle {
    position: absolute;
    left: 97px;
    top: 1087px;
    margin: 0;
    font-family: "DM Serif Display", serif;
    font-size: 40px;
    line-height: 50px;
    letter-spacing: -0.03em;
    color: var(--pink-bright);
    white-space: nowrap;
  }
</style>
</head>
<body>
<main class="post">
  <p class="intro">This 90-day plan<br>helped women over 40<br>slim down,</p>
  <p class="promise">Get a tiny waist<br>and feel sexy<br>again.</p>
  <p class="call">YOU’RE NEXT.</p>
  <svg class="sparkles" viewBox="0 0 150 140" aria-hidden="true">
    <g fill="var(--pink-bright)">
      <path d="M72 8 C75 50 78 67 128 70 C78 73 75 90 72 134 C69 90 66 73 16 70 C66 67 69 50 72 8 Z"/>
      <path d="M35 8 C36 23 38 27 55 28 C38 29 36 33 35 48 C34 33 32 29 15 28 C32 27 34 23 35 8 Z"/>
      <path d="M123 85 C124 93 125 96 135 97 C125 98 124 101 123 109 C122 101 121 98 111 97 C121 96 122 93 123 85 Z"/>
    </g>
  </svg>
  <div class="divider"></div>
  <p class="handle">@TovaMarshOnline</p>
</main>
</body>
</html>
```